Business card

Looking for modern clean business card off logo below. Very important to be clean and professional but want fun as well

Industry/Entity Type

Business

```html
<!DOCTYPE html>
<html lang="en">
<head>
<meta charset="utf-8">
<title>Hillcrest Homes – Business Card</title>
<link href="https://fonts.googleapis.com/css2?family=Michroma&family=Orbitron:wght@500;700&family=Roboto+Condensed:wght@400;700&display=swap" rel="stylesheet">
<style>
  :root {
    --bg: #1d2026;
    --sky: #86d0f1;
    --sky-deep: #72c4ea;
    --accent: #1b8fd8;
    --white: #ffffff;
    --silver-light: #fbfbfb;
    --silver-dark: #d6d8da;
    --ink: #4d4f52;
  }
  * { box-sizing: border-box; margin: 0; padding: 0; }
  html, body {
    width: 1200px; height: 860px; overflow: hidden;
    background: var(--bg);
  }
  .canvas {
    width: 1200px; height: 860px;
    display: flex; align-items: center; justify-content: center;
  }
  .card {
    width: 1000px; height: 580px;
    display: flex;
    box-shadow: 0 20px 50px rgba(0,0,0,.45);
  }
  /* Contact panel */
  .contact-panel {
    width: 560px; height: 100%;
    background: linear-gradient(135deg, var(--sky) 0%, var(--sky-deep) 100%);
    padding: 62px 0 0 60px;
    color: var(--white);
  }
  .person-name {
    font-family: "Michroma", sans-serif;
    font-size: 26px; letter-spacing: 2px;
  }
  .person-role {
    font-family: "Orbitron", sans-serif; font-weight: 500;
    font-size: 17px; color: var(--accent); margin-top: 6px;
  }
  .address {
    font-family: "Michroma", sans-serif;
    font-size: 17px; line-height: 1.5;
    margin: 44px 0 36px 60px;
  }
  .contact-list { list-style: none; }
  .contact-list li {
    display: flex; align-items: center; gap: 14px;
    font-family: "Michroma", sans-serif; font-size: 15px;
    letter-spacing: 1px; margin-bottom: 14px;
  }
  .contact-list svg { width: 20px; height: 20px; flex: none; }
  .contact-list .web { font-size: 13px; }

  /* Brand band */
  .brand-band {
    width: 200px; height: 100%;
    background: linear-gradient(90deg, var(--silver-light) 0%, var(--silver-dark) 100%);
    display: flex; align-items: center; justify-content: center;
  }
  .brand-lockup {
    writing-mode: vertical-rl; transform: rotate(180deg);
    display: flex; align-items: center; gap: 14px;
  }
  .brand-mark {
    width: 78px; height: 78px; border-radius: 50%;
    border: 7px solid var(--ink);
  }
  .brand-text { display: flex; flex-direction: column; align-items: flex-start; }
  .brand-name {
    font-family: "Roboto Condensed", sans-serif; font-weight: 700;
    font-size: 46px; color: var(--ink); line-height: 1;
  }
  .brand-tagline {
    font-family: "Roboto Condensed", sans-serif; font-weight: 400;
    font-size: 13px; color: var(--ink); margin-top: 2px;
  }

  /* Social strip */
  .social-strip {
    width: 240px; height: 100%;
    background: var(--sky);
    display: flex; align-items: center; justify-content: center;
  }
  .social-list {
    list-style: none;
    writing-mode: vertical-rl; transform: rotate(180deg);
    display: flex; flex-direction: column; gap: 24px;
  }
  .social-list li {
    display: flex; align-items: center; gap: 14px;
    font-family: "Michroma", sans-serif; font-size: 24px; color: var(--ink);
    letter-spacing: 1px;
  }
  .social-square {
    width: 30px; height: 30px; background: var(--ink); border-radius: 3px;
  }
</style>
</head>
<body>
<div class="canvas">
  <div class="card">
    <section class="contact-panel">
      <h1 class="person-name">DANIEL MORROW</h1>
      <p class="person-role">Managing Director</p>
      <p class="address">214 9th floor, Harbor<br>Lane Road KTV</p>
      <ul class="contact-list">
        <li><svg viewBox="0 0 24 24" aria-hidden="true"><path fill="#1b8fd8" d="M6.6 10.8a15 15 0 0 0 6.6 6.6l2.2-2.2c.3-.3.7-.4 1-.2 1.1.4 2.3.6 3.6.6.6 0 1 .4 1 1V20c0 .6-.4 1-1 1A17 17 0 0 1 3 4c0-.6.4-1 1-1h3.5c.6 0 1 .4 1 1 0 1.3.2 2.5.6 3.6.1.3 0 .7-.2 1z"/></svg>015 482 7390</li>
        <li><svg viewBox="0 0 24 24" aria-hidden="true"><rect x="6" y="2" width="12" height="20" rx="2" fill="#1b8fd8"/><rect x="8" y="5" width="8" height="12" fill="#86d0f1"/></svg>015 482 7391</li>
        <li><svg viewBox="0 0 24 24" aria-hidden="true"><rect x="3" y="9" width="18" height="10" rx="1" fill="#1b8fd8"/><rect x="7" y="3" width="10" height="7" fill="#1b8fd8"/><rect x="8" y="12" width="8" height="2" fill="#86d0f1"/></svg>015 482 7392</li>
        <li><svg viewBox="0 0 24 24" aria-hidden="true"><rect x="2" y="5" width="20" height="14" rx="1" fill="#1b8fd8"/><path d="M3 6l9 7 9-7" fill="none" stroke="#86d0f1" stroke-width="1.6"/></svg>dmorrow@mailbox.com</li>
        <li class="web"><svg viewBox="0 0 24 24" aria-hidden="true"><circle cx="12" cy="12" r="10" fill="#1b8fd8"/><path d="M2 12h20M12 2c3 3 3 17 0 20M12 2c-3 3-3 17 0 20" fill="none" stroke="#86d0f1" stroke-width="1.3"/></svg>www.hillcresthomes.com</li>
      </ul>
    </section>
    <section class="brand-band">
      <div class="brand-lockup">
        <span class="brand-mark" aria-hidden="true"></span>
        <div class="brand-text">
          <span class="brand-name">HILLCREST HOMES</span>
          <span class="brand-tagline">Property Management and Real Estate</span>
        </div>
      </div>
    </section>
    <section class="social-strip">
      <ul class="social-list">
        <li><span class="social-square" aria-hidden="true"></span>social.page/hillcrest</li>
        <li><span class="social-square" aria-hidden="true"></span>short.post/hillcrest</li>
      </ul>
    </section>
  </div>
</div>
</body>
</html>
```